Yard sign

I want it to look similar to this one,

change name to DRAVEK and submit new ideas

Also would like to improvise a bit. let's not make exactly the same thing

would like to change to: Connecticut #1 Company

also change phone to 203-555-0147
and website to
dravekllc.com

this is yard sign. size is 24' Width and 32' Height

Target Market(s)

Roof

Industry/Entity Type

Roofing

Requirements
Must have
• similar colors or add something new

```html
<!DOCTYPE html>
<html lang="en">
<head>
<meta charset="utf-8">
<title>DRAVEK Yard Sign</title>
<link rel="stylesheet" href="https://fonts.googleapis.com/css2?family=Anton&family=Montserrat:wght@600;700;900&display=swap">
<style>
  :root {
    --yellow: #ffe800;
    --black: #000000;
    --red: #ff0000;
    --white: #ffffff;
    --steel-dark: #3a3a3a;
    --steel-light: #d0d0d0;
    --backdrop: #e9eaec;
  }
  html, body {
    margin: 0;
    padding: 0;
    width: 1040px;
    height: 1200px;
    overflow: hidden;
    background: var(--backdrop);
  }
  .yard-sign {
    position: absolute;
    left: 100px;
    top: 40px;
    width: 840px;
    height: 1120px;
    display: block;
    box-shadow: 0 10px 30px rgba(0,0,0,0.18);
  }
  .tagline-state {
    font-family: "Anton", "Oswald", sans-serif;
    fill: var(--black);
  }
  .headline-company {
    font-family: "Montserrat", sans-serif;
    font-weight: 900;
  }
  .headline-company-shadow { fill: var(--red); }
  .headline-company-face {
    fill: url(#steel-face);
    stroke: var(--white);
    stroke-width: 5;
    paint-order: stroke fill;
  }
  .accent-stripe { stroke: var(--red); stroke-width: 8; fill: none; stroke-linejoin: miter; }
  .brand-name {
    font-family: "Anton", "Oswald", sans-serif;
    fill: var(--red);
    stroke: var(--white);
    stroke-width: 6;
    paint-order: stroke fill;
  }
  .phone-pill { fill: var(--yellow); }
  .phone-badge { fill: var(--red); stroke: var(--white); stroke-width: 5; }
  .phone-icon { fill: var(--white); }
  .phone-waves { fill: none; stroke: var(--white); stroke-width: 4; stroke-linecap: round; }
  .phone-number {
    font-family: "Anton", "Oswald", sans-serif;
    fill: var(--black);
  }
  .website {
    font-family: "Montserrat", sans-serif;
    font-weight: 600;
    fill: var(--white);
    letter-spacing: 4px;
  }
  .website-rule { stroke: var(--yellow); stroke-width: 2; }
</style>
</head>
<body>
<svg class="yard-sign" viewBox="0 0 840 1120" xmlns="http://www.w3.org/2000/svg" role="group" aria-label="DRAVEK roofing yard sign">
  <defs>
    <linearGradient id="steel-band" x1="0" y1="0" x2="1" y2="0">
      <stop offset="0" stop-color="#6f6f6f"/>
      <stop offset="0.5" stop-color="#ffffff"/>
      <stop offset="1" stop-color="#6f6f6f"/>
    </linearGradient>
    <linearGradient id="steel-face" x1="0" y1="0" x2="1" y2="1">
      <stop offset="0" stop-color="var(--steel-dark)"/>
      <stop offset="0.45" stop-color="var(--steel-light)"/>
      <stop offset="1" stop-color="var(--steel-dark)"/>
    </linearGradient>
  </defs>

  <!-- panels -->
  <rect class="panel-lower" width="840" height="1120" fill="var(--black)"/>
  <polygon class="chevron-band" points="0,0 840,0 840,452 420,568 0,452" fill="url(#steel-band)"/>
  <polygon class="panel-upper" points="0,0 840,0 840,410 420,528 0,410" fill="var(--yellow)"/>
  <polyline class="accent-stripe" points="0,474 420,592 840,474"/>

  <!-- headline -->
  <text class="tagline-state" x="420" y="158" font-size="118" text-anchor="middle" textLength="695" lengthAdjust="spacingAndGlyphs">CONNECTICUT #1</text>

  <g class="headline-company" font-size="168">
    <text class="headline-company-shadow" x="426" y="346" text-anchor="middle" textLength="700" lengthAdjust="spacingAndGlyphs">COMPANY</text>
    <text class="headline-company-face" x="420" y="341" text-anchor="middle" textLength="700" lengthAdjust="spacingAndGlyphs">COMPANY</text>
  </g>

  <!-- brand -->
  <text class="brand-name" x="420" y="828" font-size="240" text-anchor="middle" textLength="660" lengthAdjust="spacingAndGlyphs">DRAVEK</text>

  <!-- phone -->
  <rect class="phone-pill" x="110" y="860" width="660" height="96" rx="48"/>
  <circle class="phone-badge" cx="140" cy="908" r="52"/>
  <g class="phone-glyph" transform="translate(140 908) scale(0.9)">
    <path class="phone-icon" d="M-26,-14 C-26,-22 -20,-28 -14,-28 L-8,-28 L-2,-14 L-9,-8 C-6,2 2,10 9,13 L15,6 L28,12 L28,18 C28,24 22,30 14,30 C-8,28 -26,8 -26,-14 Z"/>
    <path class="phone-waves" d="M4,-20 A18,18 0 0 1 22,-2"/>
    <path class="phone-waves" d="M6,-32 A30,30 0 0 1 34,-4"/>
  </g>
  <text class="phone-number" x="465" y="938" font-size="78" text-anchor="middle" textLength="440" lengthAdjust="spacingAndGlyphs">203-555-0147</text>

  <!-- website -->
  <line class="website-rule" x1="85" y1="1040" x2="190" y2="1040"/>
  <line class="website-rule" x1="650" y1="1040" x2="755" y2="1040"/>
  <text class="website" x="420" y="1055" font-size="44" text-anchor="middle">dravekllc.com</text>
</svg>
</body>
</html>
```